Fitness Body Weight Exercises Book Cover

Need a book cover design for a new book

This book is going to market to people to get in shape by playing a fitness dice game call Rollfit The dice game

When people see the cover they should see that this is a book that can help them get in shape. We are positioning the guru as an expert inside of the fitness niche

Target Market(s)

fitness

Requirements
Must have
• The name of the book which is

"The Grand Summit Frame Regimen"

Tagline -

The Worlds #1 Resource For Combat Strength Training Using Body Weight Exercises For Men, Women and Children

__________

Featuring Rollfit, a Dice Game

___________________________
ON THE BACK COVER

Image with Oren with his gold medal
with these words
No Weights, No Problem

_____-

front cover
the image with him doing a push up should be on the front of the cover with these words

_________
Nice to have
• Maybe

"Oren Presents ...."

The Grand Summit Frame Regimen

```html
<!DOCTYPE html>
<html lang="en">
<head>
<meta charset="utf-8">
<title>The Grand Summit Frame Regimen – Book Cover</title>
<link rel="stylesheet" href="https://fonts.googleapis.com/css2?family=Oswald:wght@600;700&family=Open+Sans:wght@600;700;800&display=swap">
<style>
  :root {
    --charcoal: #2a2b2d;
    --charcoal-deep: #1b1c1e;
    --spine: #141517;
    --night: #1a2430;
    --steel: #3f5568;
    --gold: #f6e21a;
    --gold-warm: #b8902e;
    --white: #ffffff;
    --frame-line: #bfbfbf;
  }
  * { margin: 0; padding: 0; box-sizing: border-box; }
  html, body { width: 1200px; height: 833px; overflow: hidden; background: #111; }
  .cover-spread { position: relative; width: 1200px; height: 833px; overflow: hidden; font-family: "Open Sans", Arial, sans-serif; color: var(--white); }

  /* Back cover */
  .back-cover { position: absolute; left: 0; top: 0; width: 560px; height: 833px;
    background: linear-gradient(180deg, #2c2d30 0%, var(--charcoal) 55%, var(--charcoal-deep) 100%); }
  .back-panel { position: absolute; left: 82px; top: 34px; width: 415px; height: 559px;
    background: linear-gradient(180deg, #2b2c2e 0%, #37383a 100%); box-shadow: 0 0 28px rgba(0,0,0,.6); }
  .back-frame { position: absolute; left: 28px; top: 23px; width: 361px; height: 349px; border: 1px solid var(--frame-line); }
  .medal-photo { position: absolute; left: 50px; top: 45px; width: 315px; height: 320px;
    background: radial-gradient(ellipse at 50% 60%, #8a5e42 0%, #5e4030 40%, #2b2c2e 78%); }
  .back-slogan { position: absolute; left: 0; top: 410px; width: 100%; text-align: center;
    font-weight: 700; font-size: 33px; line-height: 58px; }

  /* Spine */
  .spine { position: absolute; left: 560px; top: 0; width: 71px; height: 833px;
    background: linear-gradient(90deg, #0e0f11, var(--spine) 40%, #1e2024); }
  .spine-feature { position: absolute; left: 33px; top: 17px; writing-mode: vertical-rl;
    font-size: 10px; font-weight: 600; white-space: nowrap; }
  .spine-title { position: absolute; left: 17px; top: 257px; writing-mode: vertical-rl;
    font-family: "Oswald", Impact, sans-serif; font-weight: 700; font-size: 27px; line-height: 30px;
    color: var(--gold); white-space: nowrap; }
  .spine-presenter { position: absolute; left: 23px; top: 694px; writing-mode: vertical-rl;
    font-size: 13px; font-weight: 600; white-space: nowrap; }

  /* Front cover */
  .front-cover { position: absolute; left: 631px; top: 0; width: 569px; height: 833px;
    background: linear-gradient(180deg, var(--night) 0%, #2c3d4e 14%, var(--steel) 28%, #2a3745 48%, #10141a 82%, #0a0b0d 100%); }
  .tagline { position: absolute; left: 0; top: 57px; width: 569px; text-align: center;
    font-weight: 800; font-size: 29px; line-height: 40px; text-shadow: 0 2px 4px rgba(0,0,0,.6); }
  .tagline .accent { color: var(--gold); }
  .tagline .rank { color: var(--gold); font-size: 35px; }
  .presenter { position: absolute; left: 69px; top: 257px; font-size: 20px; line-height: 28px; font-weight: 600; }
  .pushup-photo { position: absolute; left: 55px; top: 291px; width: 459px; height: 300px;
    background: radial-gradient(ellipse at 50% 45%, #a07055 0%, #6a5a50 35%, #3e4348 70%, rgba(30,35,40,0) 100%); }
  .gold-band { position: absolute; left: 0; top: 720px; width: 569px; height: 113px;
    background: radial-gradient(ellipse at 25% 100%, rgba(214,170,70,.85) 0%, rgba(150,110,40,.5) 40%, rgba(10,11,13,0) 75%); }
  .book-title { position: absolute; left: 0; top: 602px; width: 569px; text-align: center;
    font-family: "Oswald", Impact, sans-serif; font-weight: 700; font-size: 54px; line-height: 65px;
    color: var(--gold); text-transform: uppercase; text-shadow: 0 3px 6px rgba(0,0,0,.7); }
  .feature-line { position: absolute; left: 0; top: 788px; width: 569px; text-align: center;
    font-size: 15px; line-height: 22px; font-weight: 700; }
</style>
</head>
<body>
  <div class="cover-spread">
    <section class="back-cover">
      <div class="back-panel">
        <div class="back-frame"></div>
        <div class="medal-photo" role="img" aria-label="Photo of Oren smiling, wearing a cap and his gold medal"></div>
        <p class="back-slogan">No Weights,<br>No Problem</p>
      </div>
    </section>

    <section class="spine">
      <span class="spine-feature">Featuring Rollfit, a Dice Game</span>
      <span class="spine-title">THE GRAND SUMMIT FRAME REGIMEN</span>
      <span class="spine-presenter">Oren Presents ....</span>
    </section>

    <section class="front-cover">
      <p class="tagline">The Worlds <span class="rank">#1</span> Resource<br>For Combat Strength Training<br><span class="accent">Using Body Weight</span> Exercises<br>For Men, Women and Children</p>
      <p class="presenter">Oren Presents ....</p>
      <div class="pushup-photo" role="img" aria-label="Photo of Oren doing a push-up outdoors"></div>
      <div class="gold-band" role="img" aria-label="Warm golden sparkle glow along the bottom edge"></div>
      <h1 class="book-title">The Grand Summit<br>Frame Regimen</h1>
      <p class="feature-line">Featuring Rollfit, a Dice Game</p>
    </section>
  </div>
</body>
</html>
```